Menu Design Project for Fastfood Restaurant

I'm looking to redesign my existing menu card for my restaurant.
We make subs, burgers, platters, breakfast and salads among other things.
The theme colors are green, brown and yellow. It should be eye catching with a sleek new age look. The menu should prominently feature the delivery options and numbers, since the concept is highly delivery focused. Also, need to have photographs incorporated into the new menu of selected items (which is currently missing).
Design-wise, tarnwell style visual elements are a good starting point, however, similar designs will not be accepted. The design should be compatible with a4 printing folded into a5 (front and back). However, an a5 front and back is also an acceptable design format.
I have more work for specialized campaigns that i will run, and would like to continue with one designer for all my needs. Please quote "larvoni has good subs" in your reply, so i know you've read the above brief.
I'm attaching the existing menu card for an idea of what we have and the items to include
Bring on the creativity.
Reason: I am looking for more submissions. Also changing to a confirmed payment project.
Hi,
This project now has a committed payment, so i hope it's more viable for you all to submit some good designs.
20 to 40 year old professionals, lunch orders
Printing

```html
<!DOCTYPE html>
<html lang="en">
<head>
<meta charset="utf-8">
<title>larvoni menu</title>
<link href="https://fonts.googleapis.com/css2?family=Oswald:wght@500;700&family=Roboto+Condensed:wght@400;700&family=Gloria+Hallelujah&family=Dancing+Script:wght@600&display=swap" rel="stylesheet">
<style>
:root{
  --bg:#d9d4cc;
  --page:#262626;
  --page-hi:#2f2f2e;
  --orange:#e8823a;
  --green:#8cc43e;
  --brown:#8a5a3c;
  --brown-menu:#6b4a34;
  --red:#e0242b;
  --white:#f2f2ee;
  --desc:#c98a52;
  --grey-box:#6e6e6c;
  --photo-a:#c9843f;
  --photo-b:#8a6a3a;
}
*{box-sizing:border-box;margin:0;padding:0}
html,body{width:1200px;height:900px;overflow:hidden;background:var(--bg)}
body{position:relative;font-family:'Roboto Condensed',sans-serif;color:var(--white)}
.page{position:absolute;top:195px;width:360px;height:510px;background:radial-gradient(circle at 40% 30%,var(--page-hi),var(--page));overflow:hidden}
.cover{left:40px}
.spread-left{left:440px}
.spread-right{left:800px;border-left:1px solid #1a1a1a}

/* cover */
.menu-word{position:absolute;left:8px;top:10px;writing-mode:vertical-rl;font-family:'Oswald',sans-serif;font-weight:700;font-size:92px;line-height:1;color:var(--brown-menu);letter-spacing:-1px}
.hero-photo{position:absolute;left:114px;top:16px;width:222px;height:70px;border-radius:4px;background:linear-gradient(180deg,var(--photo-a),var(--photo-b))}
.brand{position:absolute;left:114px;top:88px;width:222px;text-align:center;font-family:'Oswald',sans-serif;font-weight:700;font-size:32px;line-height:1.2;color:var(--green);letter-spacing:1px}
.brand-dot{display:inline-block;width:10px;height:10px;background:var(--green);border-radius:50%;margin-left:6px;vertical-align:middle}
.tagline{position:absolute;left:104px;top:138px;font-family:'Gloria Hallelujah',cursive;color:var(--white);line-height:1}
.tagline .t1{font-size:22px;display:block}
.tagline .t2{font-size:20px;display:block;margin-left:36px}
.contact{position:absolute;left:112px;top:196px;width:226px;background:var(--red);padding:6px 10px;color:var(--white);line-height:1.05}
.contact .addr{font-size:12px}
.contact .mail{font-size:15px;font-weight:700}
.contact .tel{font-size:19px;font-weight:700}
.cols{position:absolute;left:14px;top:272px;right:12px;display:flex;gap:14px}
.col{flex:1}
.col-title{font-family:'Oswald',sans-serif;font-weight:700;font-size:22px;line-height:1;margin-bottom:8px}
.orange{color:var(--orange)}
.green{color:var(--green)}

/* items */
.item{display:grid;grid-template-columns:26px 1fr;column-gap:3px;padding:2px 0 3px;border-bottom:1px dashed rgba(232,130,58,.45)}
.price{font-size:6.5px;font-weight:700;color:var(--white);padding-top:1px}
.price small{font-size:4.5px}
.name{font-size:7px;font-weight:700;text-transform:uppercase;color:var(--white)}
.desc{grid-column:2;font-size:6px;color:var(--desc);line-height:1.15}
.item.inline{grid-template-columns:26px 88px 1fr;border-bottom:none;padding:1px 0}
.item.inline .desc{grid-column:3}

.heading{font-family:'Oswald',sans-serif;font-weight:700;line-height:1}
.spread-left .heading{font-size:40px;margin:14px 0 8px 16px}
.list{padding:0 22px 0 16px}
.fresh{font-family:'Dancing Script',cursive;font-size:15px;color:var(--red);margin-left:18px;vertical-align:middle}

.spread-right .top{padding:16px 18px 0}
.big-orange{font-size:38px;color:var(--orange)}
.sub-head{font-family:'Roboto Condensed',sans-serif;font-size:16px;color:var(--white);margin:6px 0 3px;text-transform:uppercase}
.lower{display:flex;gap:12px;padding:6px 18px 0}
.left-stack{width:120px}
.combo{text-align:center;padding:6px 0}
.combo .c1{font-family:'Oswald',sans-serif;font-weight:700;font-size:15px}
.combo .c2{font-size:6px;text-transform:uppercase}
.combo .c3{font-family:'Oswald',sans-serif;font-weight:700;font-size:16px}
.drinks{background:var(--grey-box);padding:8px 10px 10px;margin-top:4px}
.badges{display:flex;gap:10px;justify-content:center;margin-bottom:6px}
.badge{width:16px;height:16px;border-radius:50%;background:#d8d8d8}
.drinks h3{font-family:'Roboto Condensed',sans-serif;font-weight:400;font-size:13px;letter-spacing:.5px;margin:4px 0 2px}
.drink{display:grid;grid-template-columns:24px 1fr;font-size:7px}
.drink b{font-size:6.5px}
.burgers{flex:1}
.burgers .heading{font-size:36px;color:var(--brown);margin-bottom:4px}
</style>
</head>
<body>

<section class="page cover">
  <div class="menu-word">MENU</div>
  <div class="hero-photo" role="img" aria-label="Photo of a toasted sub sandwich"></div>
  <div class="brand">larvoni<span class="brand-dot"></span></div>
  <div class="tagline"><span class="t1">LARVONI</span><span class="t2">has good subs!</span></div>
  <div class="contact">
    <div class="addr">nine cedar court, shop 5</div>
    <div class="mail">order@larvonieats.com</div>
    <div class="tel">tel. 04 5550182</div>
  </div>
  <div class="cols">
    <div class="col">
      <div class="col-title orange">Mornig BITES</div>
      <div class="item"><span class="price">10 <small>AED</small></span><span class="name">Labneh Wrap</span><span class="desc">Labneh, Tomato, Cucumber, Mint, Olives</span></div>
      <div class="item"><span class="price">18 <small>AED</small></span><span class="name">Special Halloumi</span><span class="desc">Halloumi Cheese, Tomato, Cucumber, Mint, Olives</span></div>
      <div class="item"><span class="price">15 <small>AED</small></span><span class="name">Mozzarella Pesto</span><span class="desc">Fresh Mozzarella, Tomato, Pesto Sauce</span></div>
      <div class="item"><span class="price">18 <small>AED</small></span><span class="name">Greek Feta</span><span class="desc">Feta Cheese, Tomato, Cucumber, Mint, Olives</span></div>
      <div class="item"><span class="price">18 <small>AED</small></span><span class="name">Cheesy</span><span class="desc">Mixed Cheese, Tomato, Cucumber, Olives</span></div>
      <div class="item"><span class="price">22 <small>AED</small></span><span class="name">Smoked Turkey</span><span class="desc">Turkey Breast, Mozzarella, Tomato, Pickles, Corn, Mustard or Mayo Sauce</span></div>
    </div>
    <div class="col">
      <div class="col-title green">BREAKFAST</div>
      <div class="item"><span class="price">10 <small>AED</small></span><span class="name">Labneh</span><span class="desc">Labneh Plate, Olive Oil, Mint, Mix of Fresh Veggies on the side</span></div>
      <div class="item"><span class="price">12 <small>AED</small></span><span class="name">Grilled Halloumi</span><span class="desc">5 pcs, Mix of Fresh Veggies on the side</span></div>
      <div class="item"><span class="price">15 <small>AED</small></span><span class="name">Traditional Omlette</span><span class="desc">3 Eggs, Mix of Fresh Veggies on the side</span></div>
      <div class="item"><span class="price">16 <small>AED</small></span><span class="name">Cheesy Omlette</span><span class="desc">3 Eggs with cheese, Mix of Fresh Veggies on the side</span></div>
      <div class="item"><span class="price">20 <small>AED</small></span><span class="name">Larvoni Morning</span><span class="desc">Labneh, Grilled Halloumi, Thyme &amp; Oil, 2 Eggs, Mix of Vegetable</span></div>
    </div>
  </div>
</section>

<section class="page spread-left">
  <h2 class="heading green">APPETIZERS</h2>
  <div class="list">
    <div class="item"><span class="price">12 <small>AED</small></span><span class="name">Garlic Bread</span><span class="desc">3 pcs of Garlic Bread with Cheese</span></div>
    <div class="item"><span class="price">15 <small>AED</small></span><span class="name">Chicken Sticks</span><span class="desc">6 pcs with Cocktail Sauce</span></div>
    <div class="item"><span class="price">18 <small>AED</small></span><span class="name">Buffalo Wings</span><span class="desc">6 wings with Buffalo Sauce</span></div>
    <div class="item"><span class="price">15 <small>AED</small></span><span class="name">Chicken Nuggets</span><span class="desc">Plate with Ketchup, Add Cheese</span></div>
    <div class="item"><span class="price">12 <small>AED</small></span><span class="name">Potato Wedges</span><span class="desc">Plate with Honey Mustard, Add Cheese</span></div>
    <div class="item"><span class="price">25 <small>AED</small></span><span class="name">Combo Starter</span><span class="desc">2 pcs Onion Rings, 2 pcs Mozzarella Sticks, 2 pcs Boneless Chicken, Mix Fries, Ranch and Cocktail Sauce</span></div>
  </div>
  <h2 class="heading orange">SALADS<span class="fresh">As fresh as it gets!</span></h2>
  <div class="list">
    <div class="item"><span class="price">15 <small>AED</small></span><span class="name">Fattoush</span><span class="desc">Lettuce, Cucumber, Tomato, Mint, Sumac, Radish, Onion, Pomegranate and Lemon Juice</span></div>
    <div class="item"><span class="price">18 <small>AED</small></span><span class="name">Greek Salad</span><span class="desc">Lettuce, Tomato, Cucumber, Mint, Olive, Feta, Oregano, Onion and Lemon Juice + Olive Oil</span></div>
    <div class="item"><span class="price">18 <small>AED</small></span><span class="name">Caesar Salad</span><span class="desc">Lettuce, Croutons, Parmesan Cheese and Caesar Sauce. Add Grilled Chicken</span></div>
    <div class="item"><span class="price">18 <small>AED</small></span><span class="name">Crab Salad</span><span class="desc">Crab Sticks, Avocado, Fresh Mushrooms, Corn, Lettuce and Tartar Sauce</span></div>
    <div class="item"><span class="price">18 <small>AED</small></span><span class="name">Tuna Salad</span><span class="desc">Tuna, Lettuce, Corn, Carrots, Tomato, Olives, Lemon Juice and Tartar Sauce</span></div>
    <div class="item"><span class="price">18 <small>AED</small></span><span class="name">Tuna Pasta</span><span class="desc">Tuna, Three Color Pasta, Corn, Carrots and Lemon Juice</span></div>
    <div class="item"><span class="price">20 <small>AED</small></span><span class="name">Larvoni Mix</span><span class="desc">Iceberg Lettuce, Fresh Mushrooms, Tomato, Turkey, Chicken, Corn, Honey Mustard</span></div>
    <div class="item"><span class="price">18 <small>AED</small></span><span class="name">Chicken Salad</span><span class="desc">Grilled Chicken, Lettuce, Corn, Avocado, Rocca, Parmesan Cheese and Honey Mustard</span></div>
    <div class="item"><span class="price">18 <small>AED</small></span><span class="name">Chicken Pasta</span><span class="desc">Grilled Chicken, Pasta, Lettuce, Tomato, Cucumber, Corn, Parmesan Cheese and Light Mayo + Vinegar</span></div>
    <div class="item"><span class="price">18 <small>AED</small></span><span class="name">Chinese Salad</span><span class="desc">Iceberg Lettuce, Tomato, Fresh Mushrooms, Corn, Mozzarella Cheese, Noodles and Mustard + Lemon + Olive Oil</span></div>
  </div>
</section>

<section class="page spread-right">
  <div class="top">
    <h2 class="heading big-orange">SUPER BITES</h2>
    <h3 class="sub-head">Chicken Bites</h3>
    <div class="item inline"><span class="price">19 <small>AED</small></span><span class="name">Breaded Chicken</span><span class="desc">Breaded Chicken, Iceberg Lettuce, Corn, Pickles, Cheddar Cheese, BBQ and Chili Sauce</span></div>
    <div class="item inline"><span class="price">18 <small>AED</small></span><span class="name">Scalopini</span><span class="desc">Chicken, Coleslaw Salad, Corn, Pickles and Garlic Paste</span></div>
    <div class="item inline"><span class="price">18 <small>AED</small></span><span class="name">Chicken Larvoni</span><span class="desc">Grilled Chicken, Mozzarella Cheese, Corn, Iceberg Lettuce, Pickles, Light Soya Sauce</span></div>
    <div class="item inline"><span class="price">20 <small>AED</small></span><span class="name">Fajita</span><span class="desc">Chicken, Mixed Pepper, Onion, Corn, Jalapeno, Lettuce, Avocado Sauce</span></div>
    <div class="item inline"><span class="price">15 <small>AED</small></span><span class="name">Chicken Style</span><span class="desc">Crispy Chicken, Lettuce, Pickles, Tomato and Garlic Sauce</span></div>
    <div class="item inline"><span class="price">18 <small>AED</small></span><span class="name">Chicken Teriyaki</span><span class="desc">Chicken, Corn, Iceberg Lettuce, Corn, Mozzarella Cheese and Teriyaki Sauce</span></div>
    <div class="item inline"><span class="price">17 <small>AED</small></span><span class="name">Chicken Tikka</span><span class="desc">Chicken, Carrots, Red Cabbage, Mozzarella Cheese and Mint Coriander Chutney</span></div>
    <h3 class="sub-head">Beef Bites</h3>
    <div class="item inline"><span class="price">18 <small>AED</small></span><span class="name">Roast Beef</span><span class="desc">Roast Beef, Mozzarella Cheese, Tomato, Lettuce, Pickles, Mayo and Mustard</span></div>
    <div class="item inline"><span class="price">20 <small>AED</small></span><span class="name">Philly Steak</span><span class="desc">Steak, Sauteed Onion, Lettuce, Cheddar Cheese</span></div>
    <div class="item inline"><span class="price">20 <small>AED</small></span><span class="name">Juicy Steak Bite</span><span class="desc">Beef, Onion, Mixed Pepper, Mill Sauce, Fresh Cream and Ketchup</span></div>
  </div>
  <div class="lower">
    <div class="left-stack">
      <div class="combo">
        <div class="c1">COMBO MEAL</div>
        <div class="c2">Add Fries or Green Salad<br>+ Soft Drink</div>
        <div class="c3">5 AED</div>
      </div>
      <div class="drinks">
        <div class="badges"><span class="badge"></span><span class="badge"></span><span class="badge"></span></div>
        <h3>COLD DRINKS</h3>
        <div class="drink"><b>4 AED</b><span>Soft Drinks</span></div>
        <div class="drink"><b>10 AED</b><span>Fresh Juice</span></div>
        <div class="drink"><b>7 AED</b><span>Ice Tea</span></div>
        <div class="drink"><b>3 AED</b><span>Mineral Water</span></div>
        <div class="drink"><b>7 AED</b><span>Sparkling Water</span></div>
        <h3>HOT DRINKS</h3>
        <div class="drink"><b>10 AED</b><span>Café Latte</span></div>
        <div class="drink"><b>10 AED</b><span>Espresso</span></div>
        <div class="drink"><b>10 AED</b><span>Cappuccino</span></div>
        <div class="drink"><b>8 AED</b><span>Hot Chocolate</span></div>
        <div class="drink"><b>5 AED</b><span>Kinds of Tea</span></div>
      </div>
    </div>
    <div class="burgers">
      <h2 class="heading">BURGERS</h2>
      <div class="item"><span class="price">20 <small>AED</small></span><span class="name">The Original</span><span class="desc">Patty, Pickles, Tomato, Lettuce, Cocktail Sauce</span></div>
      <div class="item"><span class="price">22 <small>AED</small></span><span class="name">Cheesy Original</span><span class="desc">Patty, Pickles, Tomato, Lettuce, Cheese, Cocktail Sauce</span></div>
      <div class="item"><span class="price">25 <small>AED</small></span><span class="name">Press It</span><span class="desc">Patty, Deep Fried Mozzarella Cheese, Tomato, Homemade Sauce</span></div>
      <div class="item"><span class="price">22 <small>AED</small></span><span class="name">New Yorker</span><span class="desc">Patty, Lettuce, Tomato, Onion Rings, Swiss Cheese, Turkey</span></div>
      <div class="item"><span class="price">18 <small>AED</small></span><span class="name">Chicken Breast</span><span class="desc">Chicken Breast, Lettuce, Tomato, Garlic Mayo Sauce</span></div>
      <div class="item"><span class="price">22 <small>AED</small></span><span class="name">Supreme Chicken</span><span class="desc">Fresh Chicken Breast, Cheddar Cheese, Tomato, Lettuce, Turkey, Mayo Sauce</span></div>
      <div class="item"><span class="price">20 <small>AED</small></span><span class="name">Crunchy Chicken</span><span class="desc">Crispy Chicken Breast, Lettuce, Tomato, Swiss Cheese, Mayo Sauce</span></div>
    </div>
  </div>
</section>

</body>
</html>
```